Summer Music/Chorus/Choir Camp for Young Singers Ages 8-13

We need a flyer for a summer camp for young singers ages 8-13. We are nonprofit community children's chorus in Miami, FL. Our camp provides specialized training in music theory, sight-reading,and aural training through daily choral rehearsals in an environment that is both positive and a lot of fun! Our camp offers children the opportunity to come as they are, no matter the level of experience, and grow tremendously in their musicianship skills. In addition to this, our campers participate in song-writing, masterclasses, community performances, and media projects. The final design should be clean, fun, not too crowded, should appeal to boys and girls ages 8-13, and something someone that age would consider "cool" and not too childish. Drawings are cool, something different.
Updates

Target Market(s)

Ages 8-13 and parents of those kids.

Industry/Entity Type

Community

Requirements
Must have
• All info attached.
Nice to have
• Things that relate to music, especially related to singing/choirs
Should not have
• instruments, stock photos of children, or photos from our website (unless they are used very creatively), or photos in general. I've attached our previous camp flyer and our current organization flyer but I don't necessarily want this flyer to look like those.

```html
<!DOCTYPE html>
<html lang="en">
<head>
<meta charset="utf-8">
<title>Choral Camp Flyer</title>
<link rel="stylesheet" href="https://fonts.googleapis.com/css2?family=Arvo:wght@700&family=Montserrat:wght@600;700&family=Bebas+Neue&family=Oswald:wght@600&family=Courier+Prime:wght@700&display=swap">
<style>
:root{
  --sky:#cfeaea;
  --sky-deep:#b5dfdf;
  --cloud:#e2f3f3;
  --teal:#37807a;
  --teal-dark:#24625d;
  --ink:#173f3d;
  --text-teal:#2e6f6a;
  --red:#d93427;
  --cream:#f4e196;
  --white:#ffffff;
  --line:#1e3b3a;
}
*{margin:0;padding:0;box-sizing:border-box}
html,body{width:886px;height:1200px;overflow:hidden;background:var(--sky)}
.flyer{position:relative;width:886px;height:1200px;overflow:hidden;
  background:linear-gradient(180deg,var(--sky-deep) 0%,var(--sky) 55%,var(--cloud) 100%);
  font-family:"Montserrat",sans-serif;color:var(--text-teal)}
.backdrop{position:absolute;inset:0}
.singers-art{position:absolute;left:240px;top:35px;width:394px;height:265px;border-radius:20px 20px 0 0;
  background:linear-gradient(90deg,#e1473b 0%,#f0dc8c 50%,#e1473b 100%)}
.abs{position:absolute}
.main-circle{left:191px;top:244px;width:508px;height:508px;border-radius:50%;background:var(--teal);
  border:4px solid var(--teal-dark);box-shadow:0 0 0 8px rgba(255,255,255,.25),0 0 0 9px var(--line)}
.title-box{left:300px;top:334px;width:287px;height:85px;border:4px solid var(--teal-dark);
  display:flex;align-items:center;justify-content:center;font-family:"Arvo",serif;font-size:70px;color:var(--white);letter-spacing:2px}
.subtitle{left:191px;top:428px;width:508px;text-align:center;font-weight:700;font-size:52px;line-height:50px;color:var(--white)}
.rule{height:3px;background:#a9d6d2}
.dates{left:191px;top:566px;width:508px;text-align:center;font-family:"Courier Prime",monospace;font-weight:700}
.dates .day{font-size:42px;line-height:42px;color:var(--ink)}
.dates .time{font-size:31px;line-height:36px;color:var(--white)}
.invite{left:634px;top:242px;width:204px;height:204px;border-radius:50%;background:var(--cream);
  box-shadow:0 0 0 5px var(--sky),0 0 0 6px var(--line);display:flex;flex-direction:column;align-items:center;justify-content:center;text-align:center}
.invite .note{font-family:"Bebas Neue",sans-serif;font-size:25px;line-height:25px;color:var(--text-teal)}
.invite .cta{font-weight:700;font-size:26px;line-height:28px;color:var(--red);margin-top:4px}
.extended{left:626px;top:541px;width:274px;height:274px;border-radius:50%;background:var(--red);
  box-shadow:0 0 0 8px var(--sky),0 0 0 9px var(--line);display:flex;align-items:center;justify-content:center}
.extended p{width:190px;margin-right:6px;text-align:center;font-family:"Bebas Neue",sans-serif;font-size:31px;line-height:30px;color:var(--white)}
.price{left:21px;top:497px;width:187px;height:216px;background:var(--cream);border:10px solid var(--teal);
  box-shadow:3px 3px 0 rgba(0,0,0,.12);text-align:center;padding-top:12px}
.price .amount{font-family:"Oswald",sans-serif;font-size:66px;line-height:72px;color:var(--red)}
.price .session{font-weight:700;font-size:21px;line-height:23px;color:var(--text-teal);margin-top:4px}
.price .fine{font-family:"Bebas Neue",sans-serif;font-size:17px;line-height:18px;color:var(--ink);margin-top:10px}
.address{left:150px;top:774px;width:570px;text-align:center;font-weight:700;font-size:21px;line-height:25px}
.red-rule{left:200px;top:862px;width:477px;height:3px;background:var(--red)}
.phone{left:150px;top:876px;width:570px;text-align:center;font-weight:700;font-size:56px;line-height:68px;color:var(--ink);letter-spacing:-2px}
.email{left:150px;top:948px;width:570px;text-align:center;font-weight:700;font-size:20px;color:var(--ink)}
.org-name{left:66px;top:1030px;width:220px;font-weight:700;font-size:26px;line-height:30px;color:var(--teal);display:flex;align-items:center;gap:10px}
.org-name .dot{flex:none;width:30px;height:30px;border-radius:50%;background:var(--teal)}
.divider{left:311px;top:1007px;width:2px;height:111px;background:var(--line)}
.partner{font-weight:700;font-size:16px;color:var(--ink)}
.partner-fund{left:350px;top:1052px}
.badge{left:576px;top:1022px;width:72px;height:72px;border:3px solid var(--ink);background:var(--white)}
.partner-county{left:680px;top:1052px;display:flex;align-items:center;gap:8px}
.partner-county .mark{width:22px;height:22px;background:var(--ink)}
.footer{left:0;top:1154px;width:886px;text-align:center;font-weight:700;font-size:12px;color:var(--ink)}
</style>
</head>
<body>
<main class="flyer">
  <svg class="backdrop" width="886" height="1200" viewBox="0 0 886 1200" aria-hidden="true">
    <g fill="#c0e3e3">
      <circle cx="90" cy="140" r="110"/><circle cx="230" cy="150" r="90"/>
      <circle cx="820" cy="120" r="110"/><circle cx="60" cy="1150" r="120"/>
      <circle cx="830" cy="1140" r="110"/>
    </g>
    <circle cx="-10" cy="250" r="50" fill="#aed9d9" stroke="#1e3b3a" stroke-width="1"/>
    <g fill="none" stroke="#ffffff" stroke-width="1.5" stroke-dasharray="7 6" opacity=".8">
      <path d="M0 330 Q300 220 700 60"/>
      <path d="M0 420 Q320 300 760 20"/>
      <path d="M640 0 Q900 400 700 1000"/>
      <path d="M720 0 Q960 420 820 1200"/>
      <path d="M790 0 Q990 500 880 1200"/>
      <path d="M0 860 Q200 900 300 1000"/>
    </g>
  </svg>

  <div class="singers-art" role="img" aria-label="Illustration of three cheerful young choir singers, two girls in red dresses and a boy in a yellow shirt with suspenders"></div>

  <div class="abs main-circle"></div>
  <div class="abs title-box">MUSIC</div>
  <h1 class="abs subtitle">BLAST AT OUR<br>CHORAL CAMP</h1>
  <div class="abs rule" style="left:253px;top:561px;width:384px"></div>
  <div class="abs dates">
    <div class="day">JULY 18-29</div>
    <div class="time">9AM-3PM (M-F)</div>
  </div>
  <div class="abs rule" style="left:308px;top:648px;width:269px"></div>

  <div class="abs invite">
    <p class="note">SINGERS IN<br>GRADES 3-9 ARE<br>INVITED TO ATTEND</p>
    <p class="cta">REGISTER<br>TODAY!</p>
  </div>

  <div class="abs extended"><p>EXTENDED HOURS AVAILABLE (7:30AM-5:30PM) FOR AN EXTRA $50 PER WEEK.</p></div>

  <div class="abs price">
    <div class="amount">$300</div>
    <div class="session">FOR 2-WEEK<br>SESSION</div>
    <div class="fine">PRICE DOES NOT INCLUDE<br>LUNCH</div>
  </div>

  <p class="abs address">SOUTHBAY<br>CULTURAL ARTS CENTER, 4820 SW<br>180TH STREET MIAMI, FL 33187</p>
  <div class="abs red-rule"></div>
  <p class="abs phone">786.555.0142</p>
  <p class="abs email">INFO@BRIGHTNOTESCHORUS.ORG</p>

  <div class="abs org-name"><span class="dot"></span><span>Bright Notes Youth Chorus</span></div>
  <div class="abs divider"></div>
  <p class="abs partner partner-fund">Harbor Arts Fund</p>
  <div class="abs badge"></div>
  <div class="abs partner partner-county"><span class="mark"></span><span>Coral County</span></div>

  <p class="abs footer">BRIGHT NOTES IS A 501 (C)(3) NONPROFIT ORGANIZATION. DONATIONS MADE TO BNC ARE TAX-EXEMPT</p>
</main>
</body>
</html>
```